Velvet Orchard

We need a business card design for a new project that we are openning.

Industry/Entity Type

Business

Contact Information for Business Card

Business Card

```html
<!DOCTYPE html>
<html lang="en">
<head>
<meta charset="utf-8">
<title>Velvet Orchard – Business Card</title>
<link rel="stylesheet" href="https://fonts.googleapis.com/css2?family=Kalam:wght@400;700&display=swap">
<style>
  :root {
    --backdrop: #dcdddf;
    --navy: #28378a;
    --ink: #2a3580;
    --green: #1f9a3f;
    --yellow: #f4c81c;
    --paper: #f7f7f5;
  }
  * { margin: 0; padding: 0; box-sizing: border-box; }
  html, body { width: 1200px; height: 874px; overflow: hidden; }
  body {
    background: var(--backdrop);
    font-family: "Kalam", cursive;
    display: flex;
    flex-direction: column;
    align-items: center;
    justify-content: center;
    gap: 44px;
  }
  .card {
    width: 640px;
    height: 366px;
    border-radius: 4px;
    box-shadow: 0 6px 18px rgba(0,0,0,0.18);
    position: relative;
    overflow: hidden;
  }
  /* Front side */
  .card-front { background: var(--navy); }
  .front-name {
    position: absolute;
    left: 0; right: 0; top: 34px;
    text-align: center;
    color: var(--green);
    font-weight: 700;
    font-size: 104px;
    line-height: 0.9;
    text-transform: uppercase;
    letter-spacing: 1px;
  }
  .front-tagline {
    position: absolute;
    left: 0; right: 0; bottom: 30px;
    text-align: center;
    color: var(--yellow);
    font-size: 21px;
  }
  /* Back side */
  .card-back { background: var(--paper); }
  .back-name {
    position: absolute;
    left: 32px; top: 22px;
    color: var(--green);
    font-weight: 700;
    font-size: 50px;
    line-height: 0.9;
    text-transform: uppercase;
  }
  .back-address {
    position: absolute;
    right: 34px; top: 40px;
    text-align: right;
    color: var(--ink);
    font-size: 19px;
    line-height: 1.45;
    font-style: normal;
  }
  .contact-list {
    position: absolute;
    left: 52px; top: 168px;
    list-style: none;
    color: var(--ink);
    font-size: 30px;
    line-height: 1.5;
  }
</style>
</head>
<body>
  <section class="card card-front" aria-label="Card front">
    <h1 class="front-name">Velvet<br>Orchard</h1>
    <p class="front-tagline">Ligue-me e faça a sua encomenda | Call &amp; make your order</p>
  </section>

  <section class="card card-back" aria-label="Card back">
    <h2 class="back-name">Velvet<br>Orchard</h2>
    <address class="back-address">14/88 Linden RD<br>Marlow QLD<br>4300, Brisbane</address>
    <ul class="contact-list">
      <li>Marta: 0412555019</li>
      <li>Rafael: 0412555084</li>
      <li>Luana: (07) 5550 1234</li>
    </ul>
  </section>
</body>
</html>
```